Bright Path Flyer Design for Virtual Online Clinic. -5.5 x 8.5 inches (half sheet)

We need a clean, modern flyer design for Bright Path, a new virtual walk-in clinic based in British Columbia. The flyer will be used in libraries, pharmacies, and community centers to help residents easily access primary care through their Bright Path NFC access card.
The flyer will ask a question : NEED A DOCTOR? This should be large and attention grabbing.
The design should clearly feature a Bright Path card image (the access card) as the centerpiece and visually show how patients can use it to book appointments. The tone should feel trustworthy, healthcare-oriented, and community-friendly — clean fonts, clear spacing, and strong readability from a distance.

Side One: This card has the NFC Access Card.
NEED A DOCTOR? (Large Font, Attention Grabbing)
How to Book an Appointment using your Bright Path Card
Step 1: Tap Your Card on Your Phone
Hold your card near the back of your phone.
It will activate automatically — no app needed.
The Bright Path scheduler will open.
Step 2: Schedule Your Appointment
Select your clinical concern.
Choose your time window.
Register (only once).
Confirm your appointment.
Step 3: Relax, we’ll take care of the rest
A doctor will call during your scheduled time.
Once booked, you’ll be able to call our office.
No emails, no texts — just a real person.
It’s that simple.
Side Two:
About Bright Path
Created by Dr. Marcus Ferrigan
Bright Path was founded to make healthcare simple and convenient. Prescription renewals. Common infections. Medical notes. And so much more.
Our doctors can address 120+ health concerns virtually — providing quality care without the waiting room. No waiting rooms. Just real doctors providing real care.
Why Patients Choose Bright Path
Easy access – book and be seen from anywhere in BC.
Effortless booking – tap your Bright Path Card to begin.
Trusted physicians – every visit is with a licensed BC family doctor.
How It Works
Book your visit — choose a time window that fits your day.
Join the queue — you’ll be called when it’s your turn.
Speak directly with your doctor — simple, secure, and stress-free.
Convenient Care for Common Concerns

Additional Details.
Please find the domain to be launched soon. I've attached the NFC card file for review, it is 85.5 mm x 54 mm. The card will be glued to the flyer.
I've attached examples of flyers but they are not the look I am seeking and I am looking for creative solutions.
Thank you!
http://brightpath-example.test/

Adult Patients in British Columbia

Healthcare

• Looking for clean lines, uniform appearance, and high legibility i.e poppins

0054AA
0677BA
7BADD7
CADEEF
E8F1F8

• Need A Doctor?
• Elegant style, not too busy, clear layout.
• Clutter, look cheap - review examples.

```html
<!DOCTYPE html>
<html lang="en">
<head>
<meta charset="utf-8">
<title>Bright Path Flyer</title>
<link rel="stylesheet" href="https://fonts.googleapis.com/css2?family=Anton&family=Bebas+Neue&family=Cabin:wght@400;500&family=Arimo&family=Dancing+Script:wght@700&display=swap">
<style>
:root{
  --navy:#0054AA;
  --blue:#0677BA;
  --sky:#7BADD7;
  --mist:#CADEEF;
  --ice:#E8F1F8;
  --photo:#cfdde3;
  --page:#dcdcdd;
  --white:#ffffff;
  --edge:#555a60;
}
*{margin:0;padding:0;box-sizing:border-box}
html,body{width:1200px;height:934px;overflow:hidden}
body{background:radial-gradient(ellipse at center,#f2f2f3 0%,var(--page) 100%);position:relative;font-family:"Cabin",sans-serif}
.side{position:absolute;top:32px;width:561px;height:866px;border:1px solid var(--edge);overflow:hidden;background:var(--navy)}
.side--front{left:36px}
.side--back{left:606px}
.brand-bar{position:absolute;left:0;top:0;width:100%;height:114px;display:flex;align-items:center;padding-left:28px;gap:12px}
.side--front .brand-bar{background:var(--white);color:var(--navy)}
.side--back .brand-bar{background:var(--navy);color:var(--white)}
.brand-dot{width:14px;height:14px;border-radius:50%;background:currentColor}
.brand-name{font-family:"Cabin",sans-serif;font-weight:500;font-size:44px;letter-spacing:.5px}
.hero{position:absolute;left:0;top:114px;width:100%;height:371px;background:var(--photo)}
.hero-photo{position:absolute;top:0;height:100%;background:linear-gradient(100deg,rgba(207,221,227,0) 0%,#e9eef1 35%,#f7f8f9 60%,#dfe6ea 100%)}
.side--front .hero-photo{left:200px;width:361px}
.side--back .hero{height:321px}
.side--back .hero-photo{left:229px;width:332px}
.headline{position:absolute;left:0;top:0;color:var(--navy)}
.headline-top{position:absolute;left:119px;top:12px;font-family:"Anton",sans-serif;font-size:62px;line-height:1;letter-spacing:1px;white-space:nowrap}
.headline-script{position:absolute;left:14px;top:40px;font-family:"Dancing Script",cursive;font-size:118px;line-height:1;white-space:nowrap}
.band{position:absolute;left:0;top:485px;width:100%;height:381px;background:var(--navy)}
.step{position:absolute;color:var(--white);text-align:center;font-size:20.5px;line-height:27px}
.step h2{font-family:"Bebas Neue",sans-serif;font-weight:400;font-size:40px;line-height:1;margin-bottom:14px;letter-spacing:.5px}
.step--one{left:9px;top:450px;width:174px;height:387px;background:var(--blue);padding:14px 4px 0}
.step--two{left:183px;top:438px;width:200px;height:399px;background:var(--navy);padding:14px 2px 0}
.step--three{left:383px;top:450px;width:169px;height:387px;background:var(--blue);padding:14px 4px 0 10px;text-align:left}
.step--three h2{text-align:left;padding-left:26px}
.about{position:absolute;left:37px;top:132px;color:var(--navy);width:320px}
.about h2{font-family:"Anton",sans-serif;font-weight:400;font-size:33px;line-height:1;letter-spacing:.3px;margin-bottom:8px;white-space:nowrap}
.about p{font-family:"Arimo",sans-serif;font-size:18px;line-height:22.5px;color:var(--blue);width:300px}
.back-copy{position:absolute;left:0;top:435px;width:100%;height:431px;background:var(--navy);color:var(--white);text-align:center;padding:17px 14px 0}
.intro{font-size:20.5px;line-height:27px}
.back-copy h3{font-family:"Anton",sans-serif;font-weight:400;font-size:24px;line-height:1;margin:34px 0 24px;letter-spacing:.2px}
.reasons{list-style:none;font-size:17px;line-height:23.7px;white-space:nowrap}
</style>
</head>
<body>
<section class="side side--front">
  <header class="brand-bar"><span class="brand-dot"></span><span class="brand-name">Bright Path</span></header>
  <div class="hero">
    <div class="hero-photo" role="img" aria-label="Photo of a doctor in a white coat with stethoscope and tie, holding a blue clipboard and pen"></div>
    <h1 class="headline">
      <span class="headline-top">NEED A</span>
      <span class="headline-script">Doctor!</span>
    </h1>
  </div>
  <div class="band"></div>
  <article class="step step--one">
    <h2>Step 1</h2>
    <p>Tap Your Card on Your Phone Hold your card near the back of your phone. It will activate automatically — no app needed. The Bright Path scheduler will open.</p>
  </article>
  <article class="step step--two">
    <h2>Step 2</h2>
    <p>Schedule Your Appointment Select your clinical concern. Choose your time window. Register (only once). Confirm your appointment.</p>
  </article>
  <article class="step step--three">
    <h2>Step 3</h2>
    <p>Relax, we’ll take care of the rest A doctor will call during your scheduled time. Once booked, you’ll be able to call our office. No emails, no texts — just a real person. It’s that simple.</p>
  </article>
</section>

<section class="side side--back">
  <header class="brand-bar"><span class="brand-dot"></span><span class="brand-name">Bright Path</span></header>
  <div class="hero">
    <div class="hero-photo" role="img" aria-label="Photo of a doctor in a white coat with stethoscope, writing on a blue clipboard"></div>
  </div>
  <div class="about">
    <h2>About Bright Path</h2>
    <p>Created by Dr. Marcus Ferrigan Bright Path was founded to make healthcare simple and convenient. Prescription renewals. Common infections. Medical notes. And so much more.</p>
  </div>
  <div class="back-copy">
    <p class="intro">Our doctors can address 120+ health concerns virtually — providing quality care without the waiting room. No waiting rooms. Just real doctors providing real care.</p>
    <h3>Why Patients Choose Bright Path</h3>
    <ul class="reasons">
      <li>Easy access – book and be seen from anywhere in BC.</li>
      <li>Effortless booking – tap your Bright Path Card to begin.</li>
      <li>Trusted physicians – every visit is with a licensed BC family doctor.</li>
      <li>How It Works</li>
      <li>Book your visit — choose a time window that fits your day.</li>
      <li>Join the queue — you’ll be called when it’s your turn.</li>
      <li>Speak directly with your doctor — simple, secure, and stress-free.</li>
      <li>Convenient Care for Common Concerns</li>
    </ul>
  </div>
</section>
</body>
</html>
```